Miami based company needs a HTML creative 1 page web design

Our company, Valtrune Systems need a 1 page web design for a service that we offer, namely homekeyvault.net. It is essentially a client portal. We provide a new an exciting service for Title Companies. Instead of the closing agent handing out a paper copy of the closing documents, the buyer of the home is able to log into homekeyvault.net and view their closing documents 24/7 on a secure site. When the buyer logs in, they are also able to view the contact information for the real estate agent, lender, and that actual closing agent that was involved in the transaction.
Here is the link to our current site:
www.homekeyvault.net
USERNAME = 7463120
PASSWORD = hollis@quellmark.net
We want the site to be more creative and have a nice fresh, clean and new look. We are catering to the real estate industry so images, vectors etc could be real estate or housing related. We don't want it to look just like our current site. We need all the elements but want a creative new design with different colors (not necessarily green). The current site should just be used as a general guide.
It is also important to note that the colors should be relatively neutral as the site will be branded for each one of our clients (the Coralgate Title). Unlike our current site, the Coralgate Title's logo should be up top, not the home key vault logo. We want it to look like it is coming from the Coralgate Title. Our logo, should be on the bottom and say "powered by HomeKeyVault.net".
It is important to note that we will be loading information dynamically for the following. We wrote the code for loading it in, we just need the place holders:
1.) The Coralgate Title - logo, website, phone, fax, address. The site should be branded to the Coralgate Title.
2.) Home Key Vault - will have PDF files that the Coralgate Title uploads.
3.) The Lender - possible picture, company name, email and phone
4.) The Real Estate Agent - possible picture, company name, email and phone
5.) The Title Agent - possible picture, email and phone
Other things to note:
1.) A user may have multiple transactions. Therefore the information for the closing package, real estate agent, lender and title agent will need to be able to stack. For example, on our current site, the green accordion will stack if there are multiple transactions.
2.) It is also important to note that sometimes there wont be any information for the broker or real estate agent or title agent. On our current site for example, if there is no real estate agent, that tab is not visible.
3.) This page will be viewed on mobile, tablets and computers and will need to be designed so it can be viewed on these.
If you have any questions, please don't hesitate to contact me.
Thanks and looking forward to seeing your work.
-Wendell
Updates
Target Market(s)
Our client is the Coralgate Title. The consumers that will be logging in our the customers of the Coralgate Title (the consumers that purchased real estate and closed at the Coralgate Title).
Industry/Entity Type
Real Estate
Number of Pages Required
1 page
Font styles to use
Look and feel

```html
<!DOCTYPE html>
<html lang="en">
<head>
<meta charset="utf-8">
<title>Coralgate Title – Client Portal</title>
<link href="https://fonts.googleapis.com/css2?family=Open+Sans:wght@400;600;700&family=Bebas+Neue&display=swap" rel="stylesheet">
<style>
:root{
  --green:#5bb544;
  --green-dark:#4a9b36;
  --ink:#333333;
  --charcoal:#343538;
  --header-bg:#f4f4f6;
  --muted:#555;
  --line:#d4d4d4;
  --white:#ffffff;
}
*{margin:0;padding:0;box-sizing:border-box}
html,body{width:1200px;height:984px;overflow:hidden;background:var(--white);font-family:"Open Sans",Arial,sans-serif;color:var(--ink)}
.page{position:relative;width:1200px;height:984px}

.site-header{position:absolute;top:0;left:0;width:1200px;height:113px;background:var(--header-bg)}
.brand{position:absolute;left:100px;top:22px;display:flex;align-items:center;gap:12px}
.brand-dot{width:50px;height:50px;border-radius:50%;background:var(--green)}
.brand-name{font-size:24px;font-weight:600;color:#444;letter-spacing:-.2px}
.contact-row{position:absolute;top:12px;right:60px;display:flex;align-items:center;font-size:12.5px;color:#555}
.contact-row .item{display:flex;align-items:center;gap:8px}
.contact-row .sep{width:1px;height:18px;border-left:1px dotted #aaa;margin:0 18px}
.ribbon{position:absolute;left:744px;top:51px;width:415px;height:36px}
.ribbon-text{position:absolute;left:0;top:0;width:415px;height:36px;line-height:36px;padding-left:29px;color:var(--white);font-weight:600;font-size:18px;text-shadow:0 1px 1px rgba(0,0,0,.25)}

.hero{position:absolute;top:113px;left:0;width:1200px;height:310px;background:linear-gradient(180deg,#8e8e8e 0%,#c9c9c9 45%,#d8d8d8 70%,#bdbdbd 100%)}
.hero-figure{position:absolute;right:120px;top:20px;width:400px;height:290px;background:radial-gradient(ellipse at 60% 55%,#f2f0ee 0%,#cfcac6 50%,rgba(200,200,200,0) 75%)}
.hero-message{position:absolute;left:100px;top:71px;border-left:5px solid var(--green)}
.hero-line{display:block;height:50px;margin-bottom:3px;font-family:"Bebas Neue",Impact,sans-serif;font-size:40px;line-height:54px;color:var(--white);padding-left:19px;background:rgba(80,80,80,.82);text-shadow:0 2px 2px rgba(0,0,0,.4)}
.hero-line:nth-child(1){width:358px;clip-path:polygon(0 0,94% 0,100% 100%,0 100%)}
.hero-line:nth-child(2){width:400px;clip-path:polygon(0 0,94% 0,100% 100%,0 100%)}
.hero-line:nth-child(3){width:432px;clip-path:polygon(0 0,94% 0,100% 100%,0 100%);margin-bottom:0}
.slider-dots{position:absolute;left:580px;top:273px;display:flex;gap:7px}
.slider-dots span{width:9px;height:9px;background:var(--green);border:1px solid #fff;box-shadow:0 1px 2px rgba(0,0,0,.4)}
.slider-dots span.active{background:#111}

.welcome-bar{position:absolute;top:423px;left:0;width:1200px;height:69px;background:var(--charcoal)}
.welcome-name{position:absolute;left:100px;top:0;line-height:69px;color:var(--white);font-size:24px;font-weight:700}
.welcome-divider{position:absolute;left:417px;top:0;width:3px;height:69px;background:linear-gradient(90deg,#2a2b2d,#46474a)}
.welcome-help{position:absolute;left:443px;top:0;line-height:69px;color:#e6e6e6;font-size:16px}
.btn-start{position:absolute;left:934px;top:16px;width:166px;height:40px;background:var(--green);color:var(--white);font-size:16px;line-height:40px;text-align:center;text-decoration:none}

.packages-title{position:absolute;top:518px;left:0;width:1200px;text-align:center;font-size:27px;font-weight:700;color:#333;letter-spacing:.3px}
.package-card{position:absolute;left:188px;top:576px;width:790px;height:262px;border:1px solid var(--line);background:var(--white)}
.package-photo{position:absolute;left:0;top:0;width:395px;height:261px;background:linear-gradient(135deg,#4d4f52 0%,#6c6e70 40%,#8a8a88 70%,#5c5d5f 100%)}
.open-btn{position:absolute;left:168px;top:101px;width:60px;height:60px;border-radius:50%;border:2px solid #fff;background:var(--green);box-shadow:0 0 0 2px rgba(0,0,0,.25)}
.package-info{position:absolute;left:458px;top:62px}
.package-info h3{font-size:17px;font-weight:700;color:#333;padding-bottom:4px;border-bottom:3px solid var(--green);width:184px;margin-bottom:8px}
.package-info p{font-size:12px;color:#555;line-height:24px}
.package-info .pdf{display:flex;align-items:center;gap:6px}

.tabs{position:absolute;top:879px;left:100px;width:1000px;height:36px}
.tab{position:absolute;top:0;width:208px;height:36px;border:1px solid #ccc;background:var(--white);text-align:center;line-height:34px;font-size:17px;font-weight:700;color:#333;text-decoration:none}
.tab.active{background:var(--green);border-color:var(--green-dark);color:var(--white)}

.site-footer{position:absolute;top:953px;left:0;width:1200px;height:31px;background:var(--charcoal);color:#e0e0e0;font-size:12.5px;line-height:31px;text-align:center}
.site-footer .sep{margin:0 10px}
.site-footer a{color:#e0e0e0;text-decoration:none}
.site-footer .powered{color:#e0e0e0}
</style>
</head>
<body>
<div class="page">
  <header class="site-header">
    <div class="brand"><span class="brand-dot"></span><span class="brand-name">Coralgate Title</span></div>
    <div class="contact-row">
      <span class="item">
        <svg width="20" height="22" viewBox="0 0 20 22"><path d="M4 2 L8 2 L9 7 L6.5 8.5 C7.5 11.5 9.5 13.5 12.5 14.5 L14 12 L19 13 L19 17 C19 18 18 19 17 19 C9 19 2 12 2 4 C2 3 3 2 4 2Z" fill="#c0392b"/></svg>
        (305)555-0148
      </span>
      <span class="sep"></span>
      <span class="item">
        <svg width="20" height="16" viewBox="0 0 20 16"><rect x="0" y="2" width="20" height="14" fill="#f39c12"/><path d="M0 2 L10 10 L20 2" fill="none" stroke="#fff" stroke-width="1.5"/></svg>
        www.quellmark.net
      </span>
    </div>
    <div class="ribbon">
      <svg width="420" height="40" viewBox="0 0 420 40" style="position:absolute;left:0;top:-12px;overflow:visible">
        <path d="M405 0 L415 10 L405 10Z" fill="#cfcfd2"/>
        <path d="M0 12 L415 12 L415 48 L0 48 L12 30Z" fill="#5bb544"/>
      </svg>
      <span class="ribbon-text">Your Closing Documents @ Your Fingertips</span>
    </div>
  </header>

  <section class="hero" role="img" aria-label="Cloudy sky backdrop with a smiling woman seated at a laptop showing a house">
    <div class="hero-figure"></div>
    <div class="hero-message">
      <span class="hero-line">We would like to take</span>
      <span class="hero-line">this opportunity to thank</span>
      <span class="hero-line">you for closing with us.</span>
    </div>
    <div class="slider-dots"><span></span><span></span><span class="active"></span></div>
  </section>

  <section class="welcome-bar">
    <span class="welcome-name">Welcome Corwin Ashby</span>
    <span class="welcome-divider"></span>
    <span class="welcome-help">Is there anything we can help you with? Contact us today!</span>
    <a class="btn-start" href="#">Get Started Now</a>
  </section>

  <h2 class="packages-title">YOUR HOME KEY VAULT(S)</h2>
  <article class="package-card">
    <div class="package-photo" role="img" aria-label="Couple reviewing closing papers with an agent at a desk">
      <span class="open-btn">
        <svg width="56" height="56" viewBox="0 0 56 56"><path d="M24 38 L24 18 C24 16 27 16 27 18 L27 27 L27 24 C27 22 30 22 30 24 L30 27 L30 25 C30 23 33 23 33 25 L33 28 L33 27 C33 25 36 25 36 27 L36 34 C36 38 34 40 31 40 L27 40 C25 40 21 35 19 32 C18 30 20 29 21 30 L24 33" fill="none" stroke="#fff" stroke-width="1.8" stroke-linejoin="round"/></svg>
      </span>
    </div>
    <div class="package-info">
      <h3>CLOSING PACKAGE</h3>
      <p>14-72310 Pellham, Renata</p>
      <p>41207 Marlow Lane Naples, FL</p>
      <p class="pdf"><svg width="12" height="15" viewBox="0 0 12 15"><path d="M0 0 L8 0 L12 4 L12 15 L0 15Z" fill="#d9382f"/></svg>Home Key Vault Delia Strand</p>
    </div>
  </article>

  <nav class="tabs">
    <a class="tab active" href="#" style="left:0">CLOSING PACKAGE</a>
    <a class="tab" href="#" style="left:261px">REAL ESTATE AGENT</a>
    <a class="tab" href="#" style="left:530px">LOAN OFFICER</a>
    <a class="tab" href="#" style="left:792px">LOAN AGENT</a>
  </nav>

  <footer class="site-footer">
    © &nbsp;Copyright 2014 Valtrune Systems LLC. All rights reserved.<span class="sep">|</span><a href="#">Privacy Polacy</a><span class="sep">|</span><span class="powered">Powered by HomeKeyVault.net</span>
  </footer>
</div>
</body>
</html>
```